Cd Cover design for Chicago based record label.

Cd Cover design for a new single! Song is dedicated to exotic dancers. We do not want our artist pictures on this one. So please use your imagination. Song Title: "Velvet Hours". Thanks? Artist: Ray Castellan feat. Lil Trevane.

```html
<!DOCTYPE html>
<html lang="en">
<head>
<meta charset="utf-8">
<title>Velvet Hours – Ray Castellan feat. Lil Trevane</title>
<link rel="stylesheet" href="https://fonts.googleapis.com/css2?family=Open+Sans:wght@400;600&display=swap">
<style>
  :root {
    --ink: #060807;
    --magenta: #ff0cf5;
    --magenta-deep: #e600dc;
    --white: #ffffff;
  }
  html, body {
    margin: 0;
    padding: 0;
    width: 1163px;
    height: 1200px;
    overflow: hidden;
    background: var(--ink);
  }
  .cover {
    position: relative;
    width: 1163px;
    height: 1200px;
    background: var(--ink);
    overflow: hidden;
    font-family: "Open Sans", sans-serif;
  }
  .pole {
    position: absolute;
    left: 965px;
    top: 0;
    width: 27px;
    height: 1200px;
    background: var(--magenta);
    z-index: 2;
  }
  .dancer-art {
    position: absolute;
    left: 622px;
    top: 307px;
    width: 504px;
    height: 819px;
    border-radius: 40px;
    background: linear-gradient(180deg, var(--magenta) 0%, var(--magenta-deep) 100%);
    z-index: 1;
  }
  .credits {
    position: absolute;
    right: 226px;
    top: 92px;
    text-align: right;
    color: var(--white);
    font-weight: 600;
    z-index: 3;
  }
  .credits .artist {
    margin: 0;
    font-size: 80px;
    line-height: 1;
    letter-spacing: -1px;
  }
  .credits .featuring {
    margin: 8px 0 0;
    font-size: 56px;
    line-height: 1;
    letter-spacing: -0.5px;
  }
  .title {
    position: absolute;
    left: 92px;
    top: 400px;
    margin: 0;
    color: var(--white);
    font-weight: 400;
    font-size: 250px;
    line-height: 0.98;
    letter-spacing: -4px;
    text-transform: uppercase;
    z-index: 3;
  }
  .title span { display: block; }
</style>
</head>
<body>
  <main class="cover">
    <div class="dancer-art" role="img" aria-label="Magenta silhouette of a dancer arching backward on the pole"></div>
    <div class="pole"></div>
    <header class="credits">
      <p class="artist">Ray Castellan</p>
      <p class="featuring">feat. Lil Trevane</p>
    </header>
    <h1 class="title"><span>Velvet</span><span>Hours</span></h1>
  </main>
</body>
</html>
```